BrovaLT BIZ Card, email signature & Stationary

Professional business cards, email signatures and ms word letterhead

Target Market(s)

business owners

Industry/Entity Type

cloud hosting

Contact Information for Business Card

name title office phone number , direct line, fax email address web site

Font styles to use
Other font styles liked:
• something that compliments font in logo

```html
<!DOCTYPE html>
<html lang="en">
<head>
<meta charset="utf-8">
<title>BrovaLT Business Card</title>
<link href="https://fonts.googleapis.com/css2?family=Montserrat:wght@300;400;500;700;800&display=swap" rel="stylesheet">
<style>
  :root {
    --bg: #e6e6e6;
    --paper: #f7f7f7;
    --ink: #1d1d1d;
    --red: #e01822;
    --dark-1: #2a2a2a;
    --dark-2: #111111;
    --muted: #8a8a8a;
    --white: #ffffff;
  }
  * { margin: 0; padding: 0; box-sizing: border-box; }
  html, body { width: 1200px; height: 992px; overflow: hidden; }
  body {
    background: var(--bg);
    font-family: "Montserrat", sans-serif;
    color: var(--ink);
    position: relative;
  }
  .card {
    position: absolute;
    width: 580px;
    height: 331px;
    left: 310px;
    border-bottom: 4px solid var(--red);
    box-shadow: 0 14px 30px rgba(0,0,0,.18);
  }
  .card--front { top: 110px; background: var(--paper); }
  .card--back {
    top: 530px;
    background: radial-gradient(ellipse at 40% 20%, var(--dark-1), var(--dark-2) 70%);
  }
  .brand-name {
    font-weight: 300;
    color: var(--red);
    letter-spacing: -1px;
    line-height: 1;
  }
  .card--front .brand-name { position: absolute; left: 42px; top: 40px; font-size: 62px; }
  .card--back .brand-name {
    position: absolute; left: 0; right: 0; top: 100px;
    text-align: center; font-size: 76px;
  }
  .web-address {
    display: flex; align-items: center; gap: 8px;
    font-size: 13px; font-weight: 700; letter-spacing: 5px;
  }
  .web-address svg { width: 14px; height: 14px; flex: none; }
  .card--front .web-address { position: absolute; left: 42px; bottom: 44px; color: var(--ink); }
  .card--back .web-address {
    position: absolute; left: 50%; top: 210px; transform: translateX(-50%);
    color: var(--white);
    border: 1.5px solid #555; border-radius: 20px; padding: 6px 18px 6px 10px;
  }
  .contact-block { position: absolute; left: 342px; top: 170px; }
  .person-name { font-size: 22px; font-weight: 400; line-height: 1.05; }
  .person-name strong { font-weight: 800; }
  .person-title { font-size: 14px; font-weight: 400; margin-top: 2px; }
  .title-rule { width: 14px; height: 2px; background: var(--red); margin: 8px 0 10px; }
  .contact-list { list-style: none; }
  .contact-list li {
    display: flex; align-items: center; gap: 8px;
    font-size: 14px; font-weight: 700; line-height: 1.45;
  }
  .contact-list svg { width: 13px; height: 13px; flex: none; }
</style>
</head>
<body>

<section class="card card--front">
  <div class="brand-name">BrovaLT</div>

  <div class="web-address">
    <svg viewBox="0 0 16 16"><circle cx="8" cy="8" r="8" fill="#e01822"/><path d="M4 6c2-1 3 1 4 0s2-2 4-1M5 11c1-1 3 0 4 1" stroke="#fff" stroke-width="1.2" fill="none"/></svg>
    www.brovalt.com
  </div>

  <div class="contact-block">
    <div class="person-name">Daniel <strong>Verhoef</strong></div>
    <div class="person-title">Project Manager</div>
    <div class="title-rule"></div>
    <ul class="contact-list">
      <li>
        <svg viewBox="0 0 16 16"><path d="M3 2l3 0 1 3-2 1.5c1 2 2.5 3.5 4.5 4.5L11 9l3 1v3c-6 1-12-5-11-11z" fill="#e01822"/></svg>
        0198 765 432
      </li>
      <li>
        <svg viewBox="0 0 16 16"><rect x="4" y="1" width="8" height="14" rx="1.5" fill="none" stroke="#e01822" stroke-width="1.6"/><circle cx="8" cy="12.5" r="0.9" fill="#e01822"/></svg>
        0198 765 433
      </li>
      <li>
        <svg viewBox="0 0 16 16"><rect x="4" y="1" width="8" height="5" fill="none" stroke="#e01822" stroke-width="1.4"/><rect x="1" y="6" width="14" height="6" rx="1" fill="#e01822"/><rect x="4" y="10" width="8" height="5" fill="#fff" stroke="#e01822" stroke-width="1.4"/></svg>
        0198 765 434
      </li>
      <li>
        <svg viewBox="0 0 16 16"><rect x="1" y="3" width="14" height="10" fill="none" stroke="#e01822" stroke-width="1.6"/><path d="M1 3l7 6 7-6" fill="none" stroke="#e01822" stroke-width="1.6"/></svg>
        hello@brovalt.com
      </li>
    </ul>
  </div>
</section>

<section class="card card--back">
  <div class="brand-name">BrovaLT</div>
  <div class="web-address">
    <svg viewBox="0 0 16 16"><circle cx="8" cy="8" r="8" fill="#8a8a8a"/><path d="M4 6c2-1 3 1 4 0s2-2 4-1M5 11c1-1 3 0 4 1" stroke="#222" stroke-width="1.2" fill="none"/></svg>
    www.brovalt.com
  </div>
</section>

</body>
</html>
```